Willowbend Pharmacy Business Cards

I need a business card design and or template. Needs to convey a softer feel along with health and wellness. Please see attached logo and color scheme.

Industry/Entity Type

Pharmacy

Colors

Designer to choose colors to be used in the design.

Requirements
Must have
• I've added a second NEW colored logo I think I am going to go with the blue green logo.
• Needs to have the colors and feel of the logo attached.
• Darrel Quimby
• Pharmacy Manager
• willowbendpharmacy.example

```html
<!DOCTYPE html>
<html lang="en">
<head>
<meta charset="utf-8">
<title>Willowbend Pharmacy Business Cards</title>
<link rel="stylesheet" href="https://fonts.googleapis.com/css2?family=Montserrat:wght@600;700&family=Open+Sans:wght@400;600&display=swap">
<style>
  :root {
    --backdrop: #f1f1f1;
    --card-white: #fbfbfb;
    --leaf-green: #a0b432;
    --rose-pink: #e87a9e;
    --ink-grey: #5e5e5e;
    --soft-grey: #8a8a8a;
    --white: #ffffff;
  }
  * { margin: 0; padding: 0; box-sizing: border-box; }
  html, body {
    width: 1200px;
    height: 1146px;
    overflow: hidden;
    background: var(--backdrop);
  }
  .canvas {
    position: relative;
    width: 1200px;
    height: 1146px;
  }
  .card {
    position: absolute;
    box-shadow: 0 18px 40px rgba(0,0,0,0.12), 0 2px 6px rgba(0,0,0,0.08);
    overflow: hidden;
  }

  /* Front card */
  .card-front {
    left: 70px;
    top: 90px;
    width: 600px;
    height: 343px;
    background: var(--card-white);
  }
  .card-front .wave {
    position: absolute;
    left: 0;
    top: 0;
    width: 600px;
    height: 343px;
  }
  .wave .wave-pink { fill: var(--rose-pink); }
  .wave .wave-green { fill: var(--leaf-green); }

  .brand {
    position: absolute;
    display: flex;
    align-items: center;
    gap: 12px;
  }
  .brand-dot {
    width: 34px;
    height: 34px;
    border-radius: 50%;
    flex: none;
  }
  .brand-name {
    font-family: "Montserrat", sans-serif;
    font-weight: 700;
    white-space: nowrap;
  }
  .card-front .brand { left: 70px; top: 62px; }
  .card-front .brand-dot { background: var(--leaf-green); }
  .card-front .brand-name { font-size: 27px; color: var(--ink-grey); }
  .card-front .brand-rule {
    position: absolute;
    left: 118px;
    top: 112px;
    width: 90px;
    height: 2px;
    background: var(--leaf-green);
  }

  .contact {
    position: absolute;
    left: 196px;
    top: 136px;
    font-family: "Open Sans", sans-serif;
  }
  .contact-name {
    font-weight: 600;
    font-size: 20px;
    color: var(--ink-grey);
    line-height: 1.1;
  }
  .contact-role {
    font-size: 14px;
    color: var(--rose-pink);
    margin-top: 2px;
  }
  .contact-divider {
    width: 22px;
    height: 1px;
    background: #c9c9c9;
    margin: 9px 0 8px;
  }
  .contact-line {
    display: flex;
    align-items: center;
    gap: 8px;
    font-size: 13px;
    color: var(--ink-grey);
    line-height: 20px;
  }
  .contact-line svg { width: 12px; height: 12px; flex: none; }
  .contact-line svg path,
  .contact-line svg rect { stroke: var(--rose-pink); fill: none; stroke-width: 1.4; }
  .contact-line svg .filled { fill: var(--rose-pink); stroke: none; }

  /* Back card */
  .card-back {
    left: 730px;
    top: 470px;
    width: 343px;
    height: 600px;
    background: var(--leaf-green);
  }
  .back-inner {
    position: absolute;
    width: 600px;
    height: 343px;
    left: -128.5px;
    top: 128.5px;
    transform: rotate(90deg);
  }
  .card-back .brand { left: 70px; top: 100px; }
  .card-back .brand-dot { background: var(--white); width: 38px; height: 38px; }
  .card-back .brand-name { font-size: 30px; color: var(--white); }
  .card-back .brand-rule {
    position: absolute;
    left: 120px;
    top: 158px;
    width: 110px;
    height: 2px;
    background: var(--white);
  }
  .web-address {
    position: absolute;
    left: 120px;
    top: 196px;
    font-family: "Open Sans", sans-serif;
    font-size: 15px;
    color: var(--white);
    letter-spacing: 0.2px;
  }
</style>
</head>
<body>
<main class="canvas">

  <section class="card card-front" aria-label="Business card front">
    <svg class="wave" viewBox="0 0 600 343" aria-hidden="true">
      <path class="wave-pink" d="M0,310 C220,304 420,262 600,182 L600,343 L0,343 Z"/>
      <path class="wave-green" d="M0,318 C220,312 420,270 600,190 L600,343 L0,343 Z"/>
    </svg>

    <div class="brand">
      <span class="brand-dot"></span>
      <span class="brand-name">Willowbend Pharmacy</span>
    </div>
    <div class="brand-rule"></div>

    <div class="contact">
      <p class="contact-name">Darrel Quimby</p>
      <p class="contact-role">Pharmacy Manager</p>
      <div class="contact-divider"></div>
      <p class="contact-line">
        <svg viewBox="0 0 12 12" aria-hidden="true"><path class="filled" d="M2.2 0.8 L4.2 3 L3.2 4.4 C3.9 6 5.9 8 7.6 8.8 L9 7.8 L11.2 9.8 L9.8 11.4 C5.4 11 1 6.6 0.6 2.2 Z"/></svg>
        000-000-0000
      </p>
      <p class="contact-line">
        <svg viewBox="0 0 12 12" aria-hidden="true"><rect x="0.8" y="2.2" width="10.4" height="7.6"/><path d="M0.8 2.4 L6 6.6 L11.2 2.4"/></svg>
        darrel@willowbendpharmacy.example
      </p>
    </div>
  </section>

  <section class="card card-back" aria-label="Business card back">
    <div class="back-inner">
      <div class="brand">
        <span class="brand-dot"></span>
        <span class="brand-name">Willowbend Pharmacy</span>
      </div>
      <div class="brand-rule"></div>
      <p class="web-address">www.willowbendpharmacy.example</p>
    </div>
  </section>

</main>
</body>
</html>
```